Cool Automotive Branding Help Needed - Vantrelique Quick Detailer

We need a product label for our automotive product. The brand of this company is "Vantrelique" and the product is a "Quick Detail Spray". Attached are the current versions of the labels, the logo, as well as possible artwork we would like added. The label size is 5.5" x 7".

We would like to add the signature which is provided in the attachments as an image. We would like change "Made In America" to "Made in the USA". We would like to add the UPC code. We would like to add the following content:

"Our High Gloss Quick Detail Spray is a proprietary combination of UV protection technology and quick detail spray that produces a high gloss shine with optical clarity after every use. Designed to remove fingerprints, dust, road grime and debris while providing a high gloss shine teamed with protection."

We would like to add the QR code too.

Target Market(s)

16-50 Male, automotive

Industry/Entity Type

Automotive

Colors
ec1f27
000000
ffffff

Requirements
Must have
• Brand name, logo, all things listed in description.

```html
<!DOCTYPE html>
<html lang="en">
<head>
<meta charset="utf-8">
<title>Vantrelique Quick Detail Spray – Label Variants</title>
<link rel="stylesheet" href="https://fonts.googleapis.com/css2?family=Roboto+Condensed:wght@400;700&family=Roboto:wght@400;700&display=swap">
<style>
  :root {
    --brand-red: #ec1f27;
    --red-light: #f24b4f;
    --red-deep: #c9161d;
    --black: #000000;
    --carbon: #141414;
    --carbon-light: #232323;
    --white: #ffffff;
    --silver: #c9c9c9;
    --silver-dark: #6a6a6a;
    --backdrop: #e4e2df;
  }
  * { box-sizing: border-box; margin: 0; padding: 0; }
  html, body { width: 1014px; height: 1200px; overflow: hidden; }
  body {
    background: var(--backdrop);
    font-family: "Roboto", Arial, sans-serif;
    position: relative;
  }
  .label {
    position: absolute;
    top: 216px;
    width: 398px;
    height: 858px;
    overflow: hidden;
    box-shadow: 0 2px 10px rgba(0,0,0,0.18);
  }
  .label--classic { left: 69px; }
  .label--framed  { left: 549px; width: 406px; }

  .label__upper {
    position: absolute; left: 0; top: 0; right: 0; height: 474px;
    background: radial-gradient(ellipse at 50% 35%, var(--carbon-light), var(--carbon) 70%, var(--black));
    text-align: center;
    color: var(--white);
  }
  .label--framed .label__upper { border-top: 14px solid var(--silver); }

  .brand-mark {
    position: absolute; left: 50%; top: 30px; transform: translateX(-50%);
    width: 214px; height: 214px;
    background: linear-gradient(135deg, var(--red-light), var(--brand-red));
  }
  .label--framed .brand-mark { top: 10px; }
  .brand-mark__name {
    position: absolute; left: 0; right: 0; top: 250px;
    font-family: "Roboto Condensed", Arial, sans-serif;
    font-weight: 700; font-size: 11px; letter-spacing: 3px;
    color: var(--brand-red);
  }
  .label--framed .brand-mark__name { top: 230px; }

  .category {
    position: absolute; left: 0; right: 0; top: 286px;
    font-size: 23px; letter-spacing: 4px; font-weight: 400;
  }
  .product-name {
    position: absolute; left: 0; right: 0; top: 350px;
    font-family: "Roboto Condensed", Arial, sans-serif;
    font-weight: 700; font-size: 43px; letter-spacing: 0.5px;
    background: linear-gradient(180deg, var(--white) 40%, var(--silver));
    -webkit-background-clip: text; background-clip: text; color: transparent;
  }
  .product-type {
    position: absolute; left: 0; right: 0; top: 426px;
    font-weight: 700; font-size: 20px; letter-spacing: 1px;
  }
  .label--framed .category { top: 280px; }
  .label--framed .product-name { top: 344px; }
  .label--framed .product-type { top: 420px; }

  .label__chrome {
    position: absolute; left: 0; right: 0; top: 474px; height: 40px;
    background: linear-gradient(180deg, var(--black) 0%, var(--silver-dark) 45%, var(--white) 55%, var(--silver-dark) 70%, var(--silver) 100%);
  }
  .label__name-band {
    position: absolute; left: 0; right: 0; top: 514px; height: 42px;
    background: linear-gradient(90deg, var(--silver), var(--white) 30%, var(--white) 70%, var(--silver));
    text-align: center;
    font-family: "Roboto Condensed", Arial, sans-serif;
    font-weight: 700; font-size: 24px; letter-spacing: 6px; line-height: 42px;
    color: var(--black);
  }
  .label__red-rule {
    position: absolute; left: 0; right: 0; top: 556px; height: 26px;
    background: linear-gradient(180deg, var(--red-deep), var(--brand-red) 50%, var(--black) 60%, var(--brand-red) 75%, var(--red-deep));
  }
  .label__lower {
    position: absolute; left: 0; right: 0; top: 582px; bottom: 0;
    background: linear-gradient(90deg, var(--red-deep), var(--red-light) 50%, var(--red-deep));
    text-align: center; color: var(--black);
  }
  .signature {
    position: absolute; left: 50%; top: 30px; transform: translateX(-50%);
    width: 150px; height: 110px;
    background: linear-gradient(135deg, rgba(0,0,0,0.55), rgba(0,0,0,0.35));
    border-radius: 4px;
  }
  .signature-frame {
    position: absolute; left: 50%; top: 18px; transform: translateX(-50%);
    width: 156px; height: 150px;
    border: 1.5px solid var(--black);
  }
  .label--framed .signature { top: 37px; width: 130px; height: 112px; }
  .volume {
    position: absolute; left: 0; right: 0; top: 182px;
    font-weight: 700; font-size: 16px; line-height: 20px;
  }
  .website {
    position: absolute; left: 0; right: 0; top: 208px;
    font-weight: 700; font-size: 16px; line-height: 20px;
  }
  .label--framed .volume { top: 188px; }
  .label--framed .website { top: 214px; }
</style>
</head>
<body>
  <section class="label label--classic">
    <div class="label__upper">
      <div class="brand-mark"></div>
      <p class="brand-mark__name">VANTRELIQUE</p>
      <p class="category">AUTOMOTIVE</p>
      <h1 class="product-name">QUICK DETAIL</h1>
      <p class="product-type">SPRAY</p>
    </div>
    <div class="label__chrome"></div>
    <div class="label__name-band">VANTRELIQUE</div>
    <div class="label__red-rule"></div>
    <div class="label__lower">
      <div class="signature" role="img" aria-label="Founder's handwritten signature"></div>
      <p class="volume">474 ML</p>
      <p class="website">WWW.VANTRELIQUE.COM</p>
    </div>
  </section>

  <section class="label label--framed">
    <div class="label__upper">
      <div class="brand-mark"></div>
      <p class="brand-mark__name">VANTRELIQUE</p>
      <p class="category">AUTOMOTIVE</p>
      <h1 class="product-name">QUICK DETAIL</h1>
      <p class="product-type">SPRAY</p>
    </div>
    <div class="label__chrome"></div>
    <div class="label__name-band">VANTRELIQUE</div>
    <div class="label__red-rule"></div>
    <div class="label__lower">
      <div class="signature-frame"></div>
      <div class="signature" role="img" aria-label="Founder's handwritten signature"></div>
      <p class="volume">474 ML</p>
      <p class="website">WWW.VANTRELIQUE.COM</p>
    </div>
  </section>
</body>
</html>
```